Whitcombe Realty Corp needs a billboard design

We need to create a billboard for our company located in Radford, VA. Our company provides off-campus student housing for the students at Elmsworth College. We offer a variety of housing options (houses, town homes,apartments, and efficiencies) all of which are close to campus. Our properties come in 1, 2, 3, 4, and 5 bedroom options. Our company colors are burgundy, grey and white. we would like to push the idea of how close we are to campus. "Off-campus housing that not off the map" The billboard can be fun and geared to ages 17-25. There should also some connection to Elmsworth College.
The website should also be included whitcomberentals.example
Updates

i will add pictures to choose from.

Target Market(s)

college students

Industry/Entity Type

Real Estate

Font styles to use
Serif

Colors

Designer to choose colors to be used in the design.

Requirements
Must have
• company logo and website
• phone number 555-214-7038
• eye catching graphic not from our website. something new. if there are people there needs to be diversity.
Nice to have
• eye catching graphic that connects the viewer to Elmsworth College
• graphic could be a stylized map of the area showing properties close to campus
Should not have
• anything that could cause problems with fair housing laws

```html
<!DOCTYPE html>
<html lang="en">
<head>
<meta charset="utf-8">
<title>Whitcombe Realty – Off-Campus Housing Billboard</title>
<link rel="stylesheet" href="https://fonts.googleapis.com/css2?family=Libre+Baskerville:wght@400;700&family=Playfair+Display:wght@700;800&display=swap">
<style>
  :root {
    --burgundy: #8a1f2f;
    --ink: #161616;
    --white: #ffffff;
    --mist: #f1f0f0;
    --stage: #e6e6e6;
    --photo-warm: #d9c2a8;
    --photo-cool: #7d95b8;
  }
  html, body {
    margin: 0;
    width: 1200px;
    height: 914px;
    overflow: hidden;
    background: var(--stage);
  }
  .billboard {
    position: absolute;
    left: 30px;
    top: 122px;
    width: 1140px;
    height: 670px;
    box-shadow: 0 4px 18px rgba(0,0,0,.18);
  }
  .headline { font-family: "Playfair Display", Georgia, serif; font-weight: 800; font-size: 38px; fill: var(--white); }
  .headline-boxed { fill: var(--burgundy); }
  .brand-name { font-family: "Libre Baskerville", Georgia, serif; font-weight: 400; fill: var(--burgundy); letter-spacing: 7px; }
  .intro { font-family: "Libre Baskerville", Georgia, serif; font-size: 13px; fill: var(--burgundy); }
  .intro-lead { fill: var(--ink); font-weight: 700; }
  .offer-lead { font-family: "Libre Baskerville", Georgia, serif; font-weight: 700; font-size: 27px; fill: var(--ink); }
  .offer-detail { font-family: "Libre Baskerville", Georgia, serif; font-weight: 700; font-size: 31px; fill: var(--white); }
  .phone { font-family: "Libre Baskerville", Georgia, serif; font-weight: 700; font-size: 52px; fill: var(--burgundy); }
  .website { font-family: "Libre Baskerville", Georgia, serif; font-weight: 700; font-size: 19px; fill: var(--ink); }
</style>
</head>
<body>
<svg class="billboard" viewBox="0 0 1090 640" xmlns="http://www.w3.org/2000/svg" preserveAspectRatio="none">
  <defs>
    <linearGradient id="photoTone" x1="0" y1="0" x2="1" y2="1">
      <stop offset="0" stop-color="#cfc9c0"/>
      <stop offset=".45" stop-color="var(--photo-warm)"/>
      <stop offset="1" stop-color="var(--photo-cool)"/>
    </linearGradient>
  </defs>

  <rect class="canvas-base" width="1090" height="640" fill="var(--mist)"/>

  <rect class="hero-photo" role="img" aria-label="Photo of a diverse group of smiling students sitting together on campus steps"
        x="0" y="0" width="720" height="430" fill="url(#photoTone)"/>

  <path class="headline-panel" d="M650,0 H1090 V420 H440 C560,340 650,200 650,0 Z" fill="var(--burgundy)"/>

  <path class="logo-wave" d="M455,348 C620,270 860,225 1090,285 V640 H455 Z" fill="var(--white)"/>

  <path class="divider-wave" d="M0,390 C180,300 420,300 600,395 C780,490 960,480 1090,410 V640 H0 Z" fill="var(--burgundy)"/>
  <path class="info-area" d="M0,405 C180,318 420,318 600,412 C780,505 960,495 1090,425 V640 H0 Z" fill="var(--mist)"/>

  <g class="headline-group">
    <text class="headline" x="702" y="72">OFF-CAMPUS</text>
    <text class="headline" x="702" y="114">HOUSING THAT</text>
    <rect x="698" y="133" width="362" height="44" fill="var(--white)"/>
    <text class="headline headline-boxed" x="704" y="168">NOT OFF THE MAP</text>
  </g>

  <g class="brand">
    <text class="brand-name" x="905" y="392" font-size="34" text-anchor="middle">WHITCOMBE</text>
    <text class="brand-name" x="905" y="432" font-size="34" text-anchor="middle">REALTY</text>
  </g>

  <g class="intro-copy">
    <text class="intro" x="50" y="426"><tspan class="intro-lead">WE OFFER</tspan> A VARIETY OF HOUSING OPTIONS (HOUSES,</text>
    <text class="intro" x="50" y="448">TOWN HOMES,APARTMENTS, AND EFFICIENCIES) ALL OF</text>
    <text class="intro" x="50" y="470">WHICH ARE CLOSE TO CAMPUS.</text>
  </g>

  <g class="offer">
    <text class="offer-lead" x="50" y="515">OUR PROPERTIES COME IN</text>
    <rect x="50" y="525" width="480" height="90" fill="var(--burgundy)"/>
    <text class="offer-detail" x="64" y="564">1, 2, 3, 4, AND 5</text>
    <text class="offer-detail" x="64" y="601">BEDROOM OPTIONS.</text>
  </g>

  <line class="contact-divider" x1="613" y1="460" x2="613" y2="590" stroke="var(--burgundy)" stroke-width="1.5"/>

  <g class="contact">
    <g class="icon-phone">
      <circle cx="663" cy="527" r="17" fill="none" stroke="var(--ink)" stroke-width="2"/>
      <path d="M655,517 l5,-2 l3,6 l-3,2 q2,5 7,7 l2,-3 l6,3 l-2,5 q-12,0 -18,-18 z" fill="var(--ink)"/>
    </g>
    <text class="phone" x="690" y="547">555-214-7038</text>

    <g class="icon-web" fill="none" stroke="var(--ink)" stroke-width="1.6">
      <circle cx="663" cy="575" r="14"/>
      <ellipse cx="663" cy="575" rx="6" ry="14"/>
      <line x1="649" y1="575" x2="677" y2="575"/>
      <line x1="652" y1="567" x2="674" y2="567"/>
      <line x1="652" y1="583" x2="674" y2="583"/>
    </g>
    <text class="website" x="690" y="582">www.whitcomberentals.example</text>
  </g>
</svg>
</body>
</html>
```